TRUCKING/TRANSPORTATION COMPANY BUSINESS CARD.

We need a business card design for our trucking company based in Tupelo, MS.
It will be a double sided design.
FRONT SIDE:
We need a good looking logo with a tagline. The tagline should match the type of business.
COMPANY NAME: RW HAULAGE LLC
BACK SIDE:
The following information should be displayed on the back of the card.
Office: 555.274.0918
Mailing: 482 W. Birch Ave.
Tupelo, MS 30917
Email: rwhaulllc@mailbox-example.net
FRONT SIDE:
BACK SIDE:
Office: 555.274.0918
Mailing: 482 W. Birch Ave.
Tupelo, MS 30917

```html
<!DOCTYPE html>
<html lang="en">
<head>
<meta charset="utf-8">
<title>RW Haulage LLC – Business Card</title>
<link href="https://fonts.googleapis.com/css2?family=Archivo:wdth,wght@100..125,600..800&display=swap" rel="stylesheet">
<style>
  :root {
    --orange: #fbb040;
    --red: #c1272d;
    --navy: #1e1a5a;
    --ink: #111111;
    --white: #ffffff;
    --frame: #555555;
  }
  html, body {
    margin: 0;
    padding: 0;
    width: 1200px;
    height: 1000px;
    overflow: hidden;
    background: var(--white);
  }
  .canvas {
    position: relative;
    width: 1200px;
    height: 1000px;
    font-family: "Archivo", Arial, sans-serif;
  }
  .card {
    position: absolute;
    left: 426px;
    width: 345px;
    height: 206px;
    box-sizing: border-box;
  }
  .card-front {
    top: 259px;
    background: linear-gradient(90deg, var(--orange) 0%, var(--orange) 40%, #fde3b4 70%, var(--white) 100%);
  }
  .front-name {
    position: absolute;
    left: 0;
    right: 0;
    top: 82px;
    text-align: center;
    font-size: 28px;
    font-weight: 800;
    font-stretch: 110%;
    letter-spacing: 0.5px;
    color: var(--red);
    margin: 0;
  }
  .card-back {
    top: 505px;
    border: 1px solid var(--frame);
    background: var(--white);
  }
  .top-band {
    position: absolute;
    left: 11px;
    top: 11px;
    width: 322px;
    height: 45px;
    background: linear-gradient(90deg, var(--white) 0%, #fde3b4 40%, var(--orange) 75%, var(--orange) 100%);
  }
  .back-name {
    position: absolute;
    right: 16px;
    top: 25px;
    font-size: 11px;
    font-weight: 800;
    font-stretch: 110%;
    color: var(--red);
    margin: 0;
  }
  .contact {
    position: absolute;
    left: 15px;
    top: 64px;
    margin: 0;
    font-stretch: 125%;
    font-weight: 700;
    font-size: 14px;
    text-transform: uppercase;
  }
  .contact-row {
    display: flex;
    margin-bottom: 14px;
    line-height: 17px;
  }
  .contact-label {
    color: var(--ink);
    width: 76px;
    flex-shrink: 0;
  }
  .contact-value {
    color: var(--navy);
    margin: 0;
  }
  .contact-value.email {
    font-size: 10.5px;
    font-stretch: 110%;
  }
  .bottom-band {
    position: absolute;
    left: 11px;
    top: 175px;
    width: 322px;
    height: 18px;
    background: linear-gradient(90deg, var(--orange) 0%, var(--orange) 42%, #fde3b4 72%, var(--white) 100%);
  }
</style>
</head>
<body>
<div class="canvas">
  <section class="card card-front" aria-label="Card front">
    <p class="front-name">RW HAULAGE LLC</p>
  </section>

  <section class="card card-back" aria-label="Card back">
    <div class="top-band"></div>
    <p class="back-name">RW HAULAGE LLC</p>
    <dl class="contact">
      <div class="contact-row">
        <dt class="contact-label">Office:</dt>
        <dd class="contact-value">555.274.0918</dd>
      </div>
      <div class="contact-row">
        <dt class="contact-label">Email:</dt>
        <dd class="contact-value email">rwhaulllc@mailbox-example.net</dd>
      </div>
      <div class="contact-row">
        <dt class="contact-label">Mailing:</dt>
        <dd class="contact-value">482 W. Birch Ave. Tupelo,<br>MS 30917</dd>
      </div>
    </dl>
    <div class="bottom-band"></div>
  </section>
</div>
</body>
</html>
```